Basic images needed for business powerpoint slides

We need basic images for a powerpoint design. The designs should be clean, modern, simple and easy to read on a screen and if they were printed on paper. The images should not be overly designed (no fancy graphics or ornate fonts), but should still look professional.

Please pay attention to the attachments that have sketches of the images that are needed. In the notes section of the powerpoint slides specifies additional details for each image.

Also, please adhere to the design guidelines that are also uploaded. Only use colors and fonts that are specified. The final images should be similar to the look and feel of the images in the design guidelines.
Updates

Designers -
Thanks for all your submissions! I am reviewing all the designs with my team and will have a decision ready by Sunday evening. If you are submitting any new designs, please submit by Sunday morning EST so my team can review them.

Thanks!

Target Market(s)

business executives

Industry/Entity Type

Business

Requirements
Must have
• Must Have:
- 1. Please see the attached powerpoint for the sketches we would like to have recreated. There are specific notes in each slide with additional details.

2. Please refer to the following pages in the uploaded design guideline document:
Colors - p. 14
- Use either the bright or muted color options as specified in the color scheme on this page

Typography - p. 16-17
- Use either helvetica or arial options

Powerpoint guidelines - p.42
- see for example of the general look and feel of the company

```html
<!DOCTYPE html>
<html lang="en">
<head>
<meta charset="utf-8">
<title>Stakeholder Circles</title>
<link rel="stylesheet" href="https://fonts.googleapis.com/css2?family=Arimo:wght@400&display=swap">
<style>
  :root {
    --bg: #ffffff;
    --ring-outer: #f9efcb;
    --ring-middle: #dfe4c6;
    --ring-inner: #e3d3ad;
    --core: #d5d4ab;
    --divider: #ebe0c6;
    --highlight: #72a862;
    --muted-text: #aaa58c;
    --muted-number: #a8a48e;
    --strong-text: #111111;
  }
  html, body {
    margin: 0;
    padding: 0;
    width: 1198px;
    height: 1200px;
    overflow: hidden;
    background: var(--bg);
  }
  .diagram {
    display: block;
    width: 1198px;
    height: 1200px;
    font-family: "Arimo", Arial, Helvetica, sans-serif;
  }
  .ring-outer { fill: var(--ring-outer); }
  .ring-middle { fill: var(--ring-middle); }
  .ring-inner { fill: var(--ring-inner); }
  .core { fill: var(--core); }
  .divider { stroke: var(--divider); stroke-width: 1.4; }
  .focus-quadrant {
    fill: var(--highlight);
    filter: drop-shadow(3px 4px 3px rgba(60, 50, 30, 0.45));
  }
  .num { fill: var(--muted-number); font-size: 27px; }
  .label { fill: var(--muted-text); font-size: 13.5px; }
  .num-strong { fill: var(--strong-text); font-size: 27px; }
  .label-strong { fill: var(--strong-text); font-size: 13.5px; }
  .label-small { fill: var(--strong-text); font-size: 12.5px; }
  .num-large { fill: var(--strong-text); font-size: 31px; }
</style>
</head>
<body>
<svg class="diagram" viewBox="0 0 607 608" preserveAspectRatio="none" role="img" aria-label="Concentric stakeholder diagram with HFAC Specialists (Bio Science - Med Affairs) highlighted">
  <circle class="ring-outer" cx="303.5" cy="304" r="303"/>
  <circle class="ring-middle" cx="303.5" cy="304" r="253"/>
  <circle class="ring-inner" cx="303.5" cy="304" r="203"/>
  <circle class="core" cx="303.5" cy="304" r="152"/>

  <line class="divider" x1="100.5" y1="304" x2="506.5" y2="304"/>
  <line class="divider" x1="303.5" y1="152" x2="303.5" y2="456"/>

  <path class="focus-quadrant" d="M303.5,304 H457.5 A154,154 0 0 1 303.5,458 Z"/>

  <!-- Ring 9 -->
  <text class="num" x="208" y="44">9</text>
  <text class="label" x="294" y="27" text-anchor="middle">Franchise Lawyers</text>
  <text class="label" x="294" y="44" text-anchor="middle">Finance</text>

  <!-- Ring 8 -->
  <text class="num" x="213" y="100">8</text>
  <text class="label" x="250" y="82">Legal Analysts</text>

  <!-- Ring 7 -->
  <text class="num" x="213" y="150">7</text>
  <text class="label" x="241" y="137">Sales &amp; Marketing</text>

  <!-- Quadrant 1 -->
  <text class="num" x="245" y="192">1</text>
  <text class="label" x="262" y="217" text-anchor="middle">HFAC</text>
  <text class="label" x="262" y="233" text-anchor="middle">Specialists</text>
  <text class="label" x="262" y="251" text-anchor="middle">(Med Products-</text>
  <text class="label" x="262" y="268" text-anchor="middle">Commercial)</text>

  <!-- Quadrant 2 -->
  <text class="num" x="339" y="192">2</text>
  <text class="label" x="358" y="217" text-anchor="middle">HFAC</text>
  <text class="label" x="358" y="233" text-anchor="middle">Specialists</text>
  <text class="label" x="358" y="251" text-anchor="middle">(Bio Science-</text>
  <text class="label" x="358" y="268" text-anchor="middle">Commercial)</text>

  <!-- Quadrant 3 -->
  <text class="num" x="244" y="330">3</text>
  <text class="label" x="225" y="348" text-anchor="middle">HFAC Specialists</text>
  <text class="label" x="225" y="367" text-anchor="middle">(Med Products-</text>
  <text class="label" x="225" y="385" text-anchor="middle">Med Affairs)</text>

  <!-- Quadrant 4 (highlighted) -->
  <text class="num-strong" x="338" y="331">4</text>
  <text class="label-strong" x="374" y="351" text-anchor="middle">HFAC&#160; Specialists</text>
  <text class="label-strong" x="374" y="370" text-anchor="middle">(Bio Science-</text>
  <text class="label-strong" x="374" y="387" text-anchor="middle">Med Affairs)</text>

  <text class="num-large" x="305" y="432">5</text>
  <text class="label-small" x="333" y="417">Clinical</text>
  <text class="label-small" x="333" y="433">Trials</text>

  <!-- Ring 6 -->
  <text class="num" x="243" y="484">6</text>
  <text class="label" x="271" y="481">Scientist</text>
</svg>
</body>
</html>
```